Startup Burlesque Dance Company needs logo and website

Hello designers,
We need a logo design and a website design. The company name is "Vespera Lumina". This is a rough cut of one of the company's shows: http://clipvault.example/q7TrnoPaLk2
The design will be for a startup Burlesque dance company. The logo and website should have a simple, retro, vintage "black and white" movie feel to it. The primary purpose for the site is for marketing the dance services, highlighting pictures and video of the show(s). There will be seven basic web pages.
• Home
• About
• Shows
• Company
• Gallery
• Promo Reel
• Contact
The following links are two examples of sites we like, but since this is a competitor, the design should not be identical. It should only serve as an example of the requested style.
http://pemberlysilkrevue.example/index.cfm
http://www.brightwickcarnival.example/
In Summary, we will need the following:
1. Logo (example of ones we like are attached in Word file)
2. Web Site Design
3. Stationary ready design for business cards and letterhead
Please design to the following screen size & resolution: 1024 x 768
Reason: Decision maker has been traveling on business so our team has not been able to meet with her.
Target Market(s)
Male and Female, 21-45 years of age
Industry/Entity Type
Marketing
Look and feel

```html
<!DOCTYPE html>
<html lang="en">
<head>
<meta charset="utf-8">
<title>Vespera Lumina — Burlesque Company</title>
<link rel="stylesheet" href="https://fonts.googleapis.com/css2?family=Federo&family=Raleway:wght@400&display=swap">
<style>
  :root {
    --paper: #e9e4d6;
    --ink: #2a2522;
    --stripe-red: #7a1f1c;
    --stripe-olive: #8a8358;
    --panel: #26282b;
    --cream: #ddd3bd;
    --frame-line: rgba(226, 218, 198, 0.75);
    --spot-light: #a8946a;
    --spot-dark: #5e5036;
    --ticket: #b5362c;
    --ticket-dark: #8f261f;
    --ticket-text: #f1dcc0;
    --footer: #1c1c1d;
    --footer-text: #c9c1b2;
  }
  * { box-sizing: border-box; margin: 0; padding: 0; }
  html, body { width: 1200px; height: 1200px; overflow: hidden; }
  body { position: relative; background: var(--stripe-red); font-family: "Federo", sans-serif; }

  .site-header {
    position: absolute; left: 0; top: 0; width: 1200px; height: 80px;
    background: var(--paper);
    box-shadow: 0 2px 6px rgba(0,0,0,0.4);
    z-index: 3;
  }
  .main-nav a {
    position: absolute; top: 31px;
    font-size: 16px; letter-spacing: 0.18em; color: var(--ink);
    text-decoration: none; text-transform: uppercase;
  }
  .nav-dot { position: absolute; top: 39px; width: 3px; height: 3px; border-radius: 50%; background: var(--ink); }
  .brand {
    position: absolute; left: 470px; top: 16px; width: 260px;
    text-align: center; color: var(--stripe-red);
    font-size: 21px; letter-spacing: 0.26em; line-height: 26px; text-transform: uppercase;
  }

  .stage {
    position: absolute; left: 0; top: 80px; width: 1200px; height: 1050px;
    background: repeating-linear-gradient(90deg, var(--stripe-red) 0 46px, var(--stripe-olive) 46px 92px);
  }
  .stage::after {
    content: ""; position: absolute; inset: 0;
    background: radial-gradient(ellipse at center, rgba(0,0,0,0) 45%, rgba(0,0,0,0.55) 100%);
  }

  .ornament {
    position: absolute; left: 398px; width: 404px; height: 36px;
    background: rgba(230, 220, 196, 0.18); border-radius: 18px; z-index: 1;
  }
  .ornament.top { top: 190px; }
  .ornament.bottom { top: 1012px; }

  .outline { position: absolute; border: 1px solid var(--frame-line); z-index: 1; }
  .outline.right-shift { left: 155px; top: 210px; width: 931px; height: 784px; }
  .outline.left-shift { left: 115px; top: 249px; width: 931px; height: 785px; }

  .hero {
    position: absolute; left: 135px; top: 229px; width: 931px; height: 784px;
    background: var(--panel); border: 3px solid var(--cream);
    overflow: hidden; z-index: 2;
    box-shadow: 0 8px 30px rgba(0,0,0,0.6);
  }
  .hero-inner-frame { position: absolute; left: 17px; top: 17px; width: 891px; height: 745px; border: 1px solid var(--frame-line); }
  .spotlight-illustration {
    position: absolute; left: 145px; top: 53px; width: 640px; height: 680px; border-radius: 50%;
    background: radial-gradient(ellipse at 50% 45%, var(--spot-light) 0%, #8c7a55 55%, var(--spot-dark) 100%);
  }
  .corner { position: absolute; width: 86px; height: 82px; }
  .corner.top-left { left: 38px; top: 38px; border-left: 3px solid #8e8a82; border-top: 3px solid #8e8a82; }
  .corner.bottom-right { right: 38px; bottom: 38px; border-right: 3px solid #8e8a82; border-bottom: 3px solid #8e8a82; }

  .rule { position: absolute; left: 110px; width: 703px; height: 1px; background: rgba(221, 211, 189, 0.7); }
  .rule.r1 { top: 87px; }
  .rule.r2 { top: 290px; height: 4px; background: rgba(221, 211, 189, 0.6); }
  .rule.r3 { top: 304px; height: 4px; background: rgba(221, 211, 189, 0.6); }
  .rule.r4 { top: 520px; }

  .hero-title { position: absolute; left: 0; top: 100px; width: 925px; text-align: center; color: var(--cream); font-weight: 400; }
  .hero-title span {
    display: block; white-space: nowrap; font-size: 138px; line-height: 1;
    letter-spacing: 0.05em; text-shadow: 4px 6px 4px rgba(0,0,0,0.6);
  }
  .hero-title .line-two { margin-top: 86px; }

  .buy-tickets {
    position: absolute; left: 602px; top: 580px; width: 230px; height: 128px;
    transform: rotate(-4deg); text-decoration: none;
  }
  .buy-tickets .stub-back { position: absolute; left: -8px; top: -14px; width: 225px; height: 120px; background: var(--ticket-dark); border-radius: 8px; transform: rotate(-8deg); }
  .buy-tickets .stub {
    position: absolute; inset: 0; background: var(--ticket); border-radius: 8px;
    box-shadow: 0 4px 10px rgba(0,0,0,0.5);
  }
  .buy-tickets .stub-label {
    position: absolute; left: 24px; top: 14px; width: 182px; height: 98px;
    border: 2px solid rgba(241, 220, 192, 0.35); border-radius: 6px;
    text-align: center; color: var(--ticket-text); line-height: 1;
  }
  .stub-label .buy { display: block; font-size: 32px; letter-spacing: 0.12em; margin-top: 16px; }
  .stub-label .tix { display: block; font-size: 25px; letter-spacing: 0.06em; margin-top: 6px; }

  .site-footer {
    position: absolute; left: 0; top: 1130px; width: 1200px; height: 70px;
    background: var(--footer); color: var(--footer-text);
  }
  .copyright { position: absolute; left: 109px; top: 27px; font-family: "Raleway", sans-serif; font-size: 13px; }
  .social { position: absolute; right: 115px; top: 26px; display: flex; gap: 18px; list-style: none; }
  .social li { display: flex; align-items: center; gap: 7px; font-family: "Federo", sans-serif; font-size: 13px; letter-spacing: 0.05em; }
  .social li::before { content: ""; width: 14px; height: 14px; border-radius: 3px; background: #6a6258; }
</style>
</head>
<body>
  <header class="site-header">
    <nav class="main-nav">
      <a href="#" style="left:119px">About</a>
      <span class="nav-dot" style="left:206px"></span>
      <a href="#" style="left:246px">Shows</a>
      <span class="nav-dot" style="left:330px"></span>
      <a href="#" style="left:371px">Company</a>
      <a href="#" style="left:753px">Gallery</a>
      <span class="nav-dot" style="left:841px"></span>
      <a href="#" style="left:861px">Promo Reel</a>
      <span class="nav-dot" style="left:989px"></span>
      <a href="#" style="left:1006px">Contact</a>
    </nav>
    <div class="brand">Vespera<br>Lumina</div>
  </header>

  <main class="stage">
  </main>

  <div class="ornament top" role="img" aria-label="Decorative scrollwork flourish"></div>
  <div class="ornament bottom" role="img" aria-label="Decorative scrollwork flourish"></div>
  <div class="outline right-shift"></div>
  <div class="outline left-shift"></div>

  <section class="hero">
    <div class="spotlight-illustration" role="img" aria-label="Silhouette of a burlesque dancer in a top hat with a cane before a spotlit stage curtain"></div>
    <div class="hero-inner-frame"></div>
    <div class="corner top-left"></div>
    <div class="corner bottom-right"></div>
    <div class="rule r1"></div>
    <div class="rule r2"></div>
    <div class="rule r3"></div>
    <div class="rule r4"></div>
    <h1 class="hero-title"><span class="line-one">VESPERA</span><span class="line-two">LUMINA</span></h1>
    <a class="buy-tickets" href="#">
      <span class="stub-back"></span>
      <span class="stub"></span>
      <span class="stub-label"><span class="buy">BUY</span><span class="tix">★ TICKETS ★</span></span>
    </a>
  </section>

  <footer class="site-footer">
    <p class="copyright">© Copyright 2013 - Vespera Lumina. All rights reserved.</p>
    <ul class="social">
      <li>Socialia</li>
      <li>ClipVault</li>
      <li>Plusring</li>
    </ul>
  </footer>
</body>
</html>
```